Custom Cakes- Nonprofit Organization Stationery Set

We are looking for a FULL set stationery design for our organization.
We create custom cakes for children in foster care and work with teens and young adults who have intellectual and developmental disabilities.
We spare no expense or amount of time creating fantastic cakes for these kids.... therefore are marketing materials need to reflect the same amount of fine details.

* Business Card Design (Front/Back preferred)
* Letterhead
* Envelope
* Presentation Folder

**** Tagline: Fostering Amazing Memories
would like this to appear on business card and marketing materials

Marlene Pruitt - Founder/Executive Director
www.brightcrumb.org
info@brightcrumb.org
1-855-MY-CRUMBS
1-855-692-7862

Address is optional
PO Box 7264
Maple Hollow, GA 30187

• Contact Information
• PO Box Address, design that will go well with textured/colored business card paper
• Updated: Business cards (maybe) textured paper, foiled, embossed or colored edges

```html
<!DOCTYPE html>
<html lang="en">
<head>
<meta charset="utf-8">
<title>Bright Crumb Foundation – Letterhead</title>
<link rel="stylesheet" href="https://fonts.googleapis.com/css2?family=Open+Sans:wght@400;600;700&display=swap">
<style>
  :root {
    --backdrop: #d9d9d9;
    --paper: #ffffff;
    --ink: #2b2b2b;
    --ink-soft: #4a4a4a;
    --pink: #e5339a;
    --blue: #1aa3e0;
    --green: #5fd62c;
    --signature-tone: #ececec;
  }
  * { box-sizing: border-box; margin: 0; padding: 0; }
  html, body {
    width: 1200px; height: 1000px; overflow: hidden;
    background: var(--backdrop);
    font-family: "Open Sans", Arial, sans-serif;
    color: var(--ink);
  }
  .letterhead {
    position: absolute; left: 253px; top: 40px;
    width: 694px; height: 920px;
    background: var(--paper);
    box-shadow: 0 6px 24px rgba(0,0,0,0.18);
    overflow: hidden;
  }
  .brand {
    position: absolute; top: 44px; left: 0; right: 0;
    display: flex; align-items: center; justify-content: center; gap: 10px;
  }
  .brand-mark { width: 26px; height: 26px; background: var(--pink); }
  .brand-name { font-size: 22px; font-weight: 700; color: var(--ink); }
  .letter-body {
    position: absolute; top: 130px; left: 86px; right: 86px;
    font-size: 11.5px; line-height: 1.55; color: var(--ink-soft);
  }
  .letter-title {
    text-align: center; font-weight: 700; font-size: 12.5px;
    color: var(--ink); margin-bottom: 30px;
  }
  .letter-body p { margin-bottom: 16px; }
  .signature {
    display: block; width: 150px; height: 34px;
    background: var(--signature-tone); margin: 26px 0 4px;
  }
  .signer { font-size: 10px; color: var(--ink-soft); }
  .contact-line {
    position: absolute; left: 86px; right: 40px; top: 784px;
    font-size: 9.5px; font-weight: 600; color: var(--ink); white-space: nowrap;
  }
  .footer-band {
    position: absolute; left: 0; right: 0; bottom: 0; height: 110px;
    display: flex;
  }
  .band-dots { flex: 1; background: var(--pink); }
  .band-stripes { flex: 1; background: linear-gradient(90deg, var(--blue), var(--green)); }
</style>
</head>
<body>
  <main class="letterhead">
    <header class="brand">
      <span class="brand-mark"></span>
      <span class="brand-name">Bright Crumb Foundation</span>
    </header>

    <section class="letter-body">
      <h1 class="letter-title">Lorem ipsum dolor sit amet, ei eros vidit sonet eum</h1>
      <p>Lorem ipsum dolor sit amet, ei eros vidit sonet eum, sed ea aliquam offendit. Reque quando labitur nec in, no solum ceteros est. Accumsan pertinacia an qui. Te vidisse recteque pro, cu per habemus officiis, eos ex malis prodesset omittantur. Appetere principes eloquentiam vis ei, an mea alia petentium dignissim, is justo omnium duo.</p>
      <p>Movet laoreet delicatissimi cum id. Essent dissentiet cu cum, atqui augue iriure qui ea. Liber propriae et sed. Euismod ornatus scaevola ei pro.</p>
      <p>Verterem interesset disputationi vim et, laudem persecuti quo eu. Mea viderer vulputate ut. Ad scripta scaevola appetere usu, omnium forensibus sed cu, dolorum admodum postulant mea ei. Eos ut ubique graeco insolens, etiam electram assentior cum at.</p>
      <p>In eos solum verterem facilisis, magna scaevola explicari has ex, at vidisse percipitur cum. At dicam postea luptatum sea, sed te timeam principes disputando, postea scaevola eloquentiam quo eu. Cetero concludaturque cu ius, nam erat detraxit ut, in his cetero vocent erroribus. Eu sint nulla comprehensam qui. Dolor dolorum splendide ei est, id usu inani liber deterruisset.</p>
      <p>Omnis intellegat intellegam duo cu, no ornatus partiendo referrentur has. Verterem interesset disputationi vim et, laudem persecuti quo eu. Mea viderer vulputate ut. Ad scripta scaevola appetere usu, omnium forensibus sed cu, dolorum admodum postulant mea ei. Eos ut ubique graeco insolens, etiam electram assentior cum at.</p>
      <p>Omnis intellegat intellegam duo cu, no ornatus partiendo referrentur has.</p>
      <span class="signature" role="img" aria-label="Handwritten signature of Marlene Pruitt"></span>
      <p class="signer">Marlene Pruitt, Founder/Executive Director</p>
    </section>

    <footer>
      <p class="contact-line">1-855-MY-CRUMBS / 1-855-692-7862 / PO Box 7264 Maple Hollow, GA 30187 / info@brightcrumb.org / www.brightcrumb.org</p>
      <div class="footer-band">
        <div class="band-dots" role="img" aria-label="Pink band with white polka dot pattern"></div>
        <div class="band-stripes" role="img" aria-label="Band of diagonal blue and green stripes"></div>
      </div>
    </footer>
  </main>
</body>
</html>
```